Redesign lumavexin.org for Shopify (Coded in Liquid)

The existing website has been up since 2013. The content is still good (text) but we need a new logo and a complete overhaul of all of the graphics. We just completed our new testing lab for verifying all new products for review. We would like the website to look very science and medical based. We will also be selling all of the products we review to sponsor our website. We have our own full stack developers, but we simply don't have the available personnel to get this project started. For reference we really like some of the animated and interactive text options available on the pixmarrow.com CMS, but we need to have the integration of the Shopify platform, as it works well with our other sites. So the final website must be in Shopify.Lumavexin.org is part of a larger company Halvorn Study Collective, so we like that reflected in the website somehow. Some necessary features we would like would be a message board and seamless integration with social media IG, Chatterly, ect... This way people can leave comments or login via Chatterly to place orders. The website needs to look great on both desktop and mobile.Please use www.lumavexin.org for all of your content. The winning designer will also have the option to overhaul our Chatterly page.Please design this site using the limitations of Shopify, and the Liquid template system they require.
Updates

Lumavexin.org was last updated in 2016. Please don't use old artwork, we used in 2016. Look for new artwork on the web. I have received entries using our old artwork, some of the products on our old website have new labels. For instance the featured 2016 best of product Dolvanix has a new label. Since this website is a review website, try to funnel users to read our reviews for different catogories, best price, highest strength, ect. No buy now on the home page. Since we are now selling the products we review on the website, we will no longer have a where to buy. Please look for new stock photography and or video on serrapeptase, visitors to our new website need to feel like the website is new not a recycled version of the old website. Please create a simple yet new logo for (KTB) Korvath Testing Bureau. Please be sure to include lots of areas for social media interaction. Most importantly get people to join our mailing lists above all else, so we can send them updates.

Target Market(s)

Consumers, Doctors and researchers

Industry/Entity Type

Biotechnology

Coding

Coded - Design and coding required

Number of Pages Required

3 page

Colors

Designer to choose colors to be used in the design.

Requirements
Must have
• Coded into Shopify (liquid) if you have never coded in Shopify do not apply please
• Animated text header see (https://www.qelt.com)
• Message board
• Mobile Friendly
• Lots of Icons and Categories (not text heavy home page)
• Social Media sections
• Consumer rating section
• Shopping Cart
Nice to have
• Enzyme and other related Video
• Interactive icons (mouse over) ect...
• Animated Text (when Scrolling)
Should not have
• Templates I find on other websites including Pinterest and Searchnest
• DNA pictures
• Other unrelated generic medical stock images
• Maps Searchnest or otherwise. They only buy from us

```html
<!DOCTYPE html>
<html lang="en">
<head>
<meta charset="utf-8">
<title>Lumavexin.org – Korvath Testing Bureau</title>
<link rel="stylesheet" href="https://fonts.googleapis.com/css2?family=Poppins:wght@300;400;500;600;700&family=Open+Sans:wght@400;600;700;800&family=Roboto:wght@400&display=swap">
<style>
:root{
  --hero-blue:#1d2285;
  --brand-blue:#1f2a8c;
  --button-blue:#1c2590;
  --teal:#0b5d79;
  --grey-band:#ebebeb;
  --dark-panel:#474747;
  --footer:#2d2d2d;
  --text:#555;
  --text-dark:#222;
  --white:#fff;
}
*{margin:0;padding:0;box-sizing:border-box}
html,body{width:1200px;height:2859px;overflow:hidden}
body{position:relative;font-family:"Poppins",sans-serif;color:var(--text);background:var(--white)}
.abs{position:absolute}
a{color:inherit}

/* hero */
.hero{left:0;top:0;width:1200px;height:680px;background:var(--hero-blue)}
.hero-visual{left:0;top:110px;width:560px;height:570px;background:radial-gradient(circle at 35% 55%,#7d9ce0 0%,#3c5bbf 30%,#23308f 60%,rgba(29,34,133,0) 80%)}
.logo{left:90px;top:28px;font:700 24px "Poppins",sans-serif;color:var(--white);letter-spacing:.3px}
.menu-toggle{left:1092px;top:36px;width:17px}
.menu-toggle span{display:block;height:2px;background:var(--white);margin-bottom:4px}
.hero-copy{right:92px;top:250px;text-align:right;color:var(--white);font-family:"Open Sans",sans-serif}
.hero-copy .lead{font-size:40px;font-weight:400;line-height:1}
.hero-copy .big{font-size:96px;font-weight:800;line-height:1;margin-top:6px;letter-spacing:-1px}
.hero-copy .sub{font-size:42px;font-weight:400;line-height:1.1;margin-top:-2px}
.hero-copy .small{font-size:20px;font-weight:600;margin-top:14px}

/* intro boxes */
.what-box{left:89px;top:428px;width:485px;height:252px;background:var(--teal);color:var(--white);padding:56px 53px 0}
.what-box h2{font:600 26px "Poppins",sans-serif;margin-bottom:12px}
.what-box p{font-size:13px;line-height:19.5px}
.btn-light{display:inline-flex;align-items:center;gap:8px;background:var(--white);color:var(--brand-blue);font-size:12px;padding:9px 16px;margin-top:13px;text-decoration:none}
.grey-band{left:0;top:680px;width:1200px;height:283px;background:var(--grey-band)}
.about{left:90px;top:752px;width:420px}
.about h2{font:600 26px "Poppins",sans-serif;color:var(--brand-blue);margin-bottom:10px}
.about p{font-size:13px;line-height:19.5px;color:#666}
.about a{display:inline-block;font-size:12.5px;color:var(--brand-blue);margin-top:13px}
.feature-panel{left:574px;top:589px;width:534px;height:374px;background:var(--dark-panel)}
.feature-photo{left:836px;top:589px;width:272px;height:374px;background:linear-gradient(180deg,#9a9a9a 0%,#5e5e5e 55%,#1e1e1e 100%)}
.feature-copy{left:611px;top:713px;color:var(--white)}
.feature-copy h3{font:600 26px "Poppins",sans-serif;margin-bottom:8px}
.feature-copy p{font-size:13px;line-height:20px}
.btn-blue{display:inline-flex;align-items:center;gap:12px;background:var(--button-blue);color:var(--white);font-size:12.5px;padding:10px 20px;margin-top:13px;text-decoration:none}

/* categories */
.cat{top:1041px;height:304px;border:1px dashed #cfcfcf;text-align:center;padding-top:40px}
.cat.active{border-color:#222}
.cat svg{width:56px;height:56px}
.cat h4{font:400 18px "Poppins",sans-serif;color:var(--text-dark);margin-top:8px}
.cat p{font-size:13px;line-height:19.5px;color:#777;margin:12px auto 0;width:200px}
.outline-btn{display:inline-block;width:122px;height:35px;line-height:33px;border:1px solid var(--button-blue);color:var(--button-blue);font-size:13px;text-decoration:none;position:absolute;left:50%;margin-left:-61px;top:230px}
.cat.active .outline-btn{background:var(--button-blue);color:var(--white)}

/* enteric */
.lab-photo{left:91px;top:1415px;width:424px;height:268px;background:linear-gradient(120deg,#d9dde3 0%,#bcc4cf 45%,#7e8aa0 100%)}
.enteric{left:575px;top:1412px;width:533px}
.enteric h2{font:600 26px "Poppins",sans-serif;color:var(--brand-blue);margin-bottom:14px}
.enteric p{font:400 13.3px/22.2px "Roboto",sans-serif;color:#666;text-align:justify}
.enteric .outline-btn{position:static;margin:12px 0 0;width:122px;text-align:center}

/* blog */
.section-title{left:0;width:1200px;text-align:center;font:600 26px "Poppins",sans-serif;color:var(--brand-blue)}
.post{top:1809px;width:321px;height:402px;background:#f7f7f7}
.post-img{height:222px;position:relative}
.post-date{position:absolute;left:0;bottom:0;background:var(--button-blue);color:var(--white);font-size:14.5px;padding:4px 15px;width:114px}
.post-body{padding:18px 17px 0}
.post-body h3{font:600 19px "Poppins",sans-serif;color:var(--brand-blue);margin-bottom:6px}
.post-body p{font-size:15px;line-height:21.5px;color:#666}
.post-body a{display:inline-block;font-size:12.5px;color:var(--brand-blue);margin-top:8px}

/* testimonial */
.avatar{left:580px;top:2319px;width:40px;height:40px;border-radius:50%;background:#e8b7ae}
.quote{left:290px;top:2377px;width:620px;text-align:center;font-size:13px;line-height:19.5px;color:#666}
.client{left:0;top:2437px;width:1200px;text-align:center;font-size:13px;color:#222}
.client small{display:block;font-size:9px;color:#888;margin-top:-2px}
.dots{left:586px;top:2480px;display:flex;gap:9px}
.dots span{width:3px;height:3px;border-radius:50%;background:#ccc}
.dots span.on{background:var(--button-blue)}

/* footer */
.footer{left:0;top:2553px;width:1200px;height:306px;background:var(--footer);color:var(--white)}
.f-logo{left:88px;top:2639px;font:700 25px "Poppins",sans-serif;color:var(--white)}
.f-about{left:90px;top:2683px;width:270px;font-size:13px;line-height:19.5px;color:#ddd}
.f-col h5{font:600 16px "Poppins",sans-serif;color:var(--white);margin-bottom:17px}
.f-links li{list-style:none;font-size:12px;color:#eee;margin-bottom:14.5px}
.f-social li{list-style:none;display:flex;align-items:center;gap:9px;font-size:12.5px;color:#eee;margin-bottom:11px}
.f-social span.dot{width:27px;height:27px;border-radius:50%;display:inline-block}
.f-news p{font-size:12.5px;line-height:19.5px;color:#eee;width:220px}
.f-input{margin-top:14px;width:245px;height:35px;background:var(--white);color:#999;font-size:10.5px;padding:11px 14px 0 35px;position:relative}
.f-input svg{position:absolute;left:14px;top:13px}
.f-send{margin-top:11px;display:inline-block;background:var(--button-blue);color:var(--white);font-size:12px;padding:8px 15px}
.f-rule{left:89px;top:2810px;width:1020px;height:1px;background:#444}
.copyright{left:0;top:2829px;width:1200px;text-align:center;font-size:13px;color:#eee}
.to-top{left:1140px;top:2783px;width:35px;height:35px;border-radius:50%;background:var(--button-blue);display:flex;align-items:center;justify-content:center}
</style>
</head>
<body>

<section class="abs hero"></section>
<div class="abs hero-visual" role="img" aria-label="Close-up illustration of an enzyme particle with spiked surface in blue tones"></div>
<div class="abs logo">LUMAVEXIN.KTB</div>
<div class="abs menu-toggle"><span></span><span></span><span></span></div>
<div class="abs hero-copy">
  <div class="lead">FOR MORE THAN</div>
  <div class="big">25 YEARS,</div>
  <div class="sub">Serrapeptase has been used by</div>
  <div class="small">Millions of people concerned about their health.</div>
</div>

<div class="abs grey-band"></div>
<div class="abs what-box">
  <h2>What is Serrapeptase?</h2>
  <p>Serrapeptase is a proteolytic enzyme that is also known as serrapeptidase, serratiopeptidase, serratia peptidase, nicolase, the super enzyme, and the miracle enzyme.<br>This enzyme is produced by non-pathogenic bacteria</p>
  <a class="btn-light" href="#">READ MORE <svg width="5" height="7" viewBox="0 0 5 7"><path d="M0 0L5 3.5L0 7Z" fill="currentColor"/></svg></a>
</div>
<div class="abs about">
  <h2>About Us</h2>
  <p>For more than 25 years, Serrapeptase has been used by millions of people concerned about their health. Originally, Serrapeptase was exclusively used in Asia and Europe due to its anti-inflammatory activity, but when the benefits</p>
  <a href="#">READ MORE</a>
</div>
<div class="abs feature-panel"></div>
<div class="abs feature-photo" role="img" aria-label="Black and white portrait photograph of the featured doctor"></div>
<div class="abs feature-copy">
  <h3>Dr. Ansel Varrick</h3>
  <p>Dr. Ansel Varrick featured in<br>April 1997</p>
  <a class="btn-blue" href="#">VIEW DETAIL <svg width="5" height="7" viewBox="0 0 5 7"><path d="M0 0L5 3.5L0 7Z" fill="currentColor"/></svg></a>
</div>

<div class="abs cat" style="left:93px;width:228px">
  <svg viewBox="0 0 56 56" fill="none" stroke="#222" stroke-width="1.6"><path d="M30 8h16v16L22 48 8 34z"/><circle cx="39" cy="15" r="3"/><path d="M18 34l10-10M22 38l8-8"/></svg>
  <h4>Compare Brands</h4>
  <p>With so many choices of Serra-peptase, it can be difficult to decide which product</p>
  <a class="outline-btn" href="#">Learn More</a>
</div>
<div class="abs cat active" style="left:349px;width:236px">
  <svg viewBox="0 0 56 56" fill="none" stroke="#222" stroke-width="1.6"><circle cx="28" cy="22" r="14"/><circle cx="28" cy="22" r="10"/><path d="M26 18l3-2v12M19 33l-7 13 6-1 3 5 6-12M37 33l7 13-6-1-3 5-6-12"/></svg>
  <h4>Best Serrapeptase</h4>
  <p>With so many choices of Serra-peptase, it can be difficult to decide which product</p>
  <a class="outline-btn" href="#">Learn More</a>
</div>
<div class="abs cat" style="left:609px;width:237px">
  <svg viewBox="0 0 56 56" fill="none" stroke="#222" stroke-width="1.6"><circle cx="28" cy="28" r="17"/><circle cx="28" cy="28" r="4"/><path d="M28 24V11M31 30l11 7M25 30l-11 7M28 11c6 3 8 9 3 13M42 37c-6 2-11-1-11-7M14 37c0-6 5-10 11-7"/></svg>
  <h4>The Dangers of Enteric</h4>
  <p>If you knew your Serrapeptase supplement was Enteric Coated with plastic</p>
  <a class="outline-btn" href="#">Learn More</a>
</div>
<div class="abs cat" style="left:869px;width:237px">
  <svg viewBox="0 0 56 56" fill="none" stroke="#222" stroke-width="1.6"><rect x="8" y="8" width="26" height="18"/><path d="M13 14h16M13 19h12M14 26l-2 6 7-6"/><rect x="22" y="30" width="26" height="18"/><circle cx="35" cy="37" r="3"/><path d="M30 45c1-4 9-4 10 0"/></svg>
  <h4>Public Message Boards</h4>
  <p>With so many choices of Serra-peptase, it can be difficult to decide which product</p>
  <a class="outline-btn" href="#">Learn More</a>
</div>

<div class="abs lab-photo" role="img" aria-label="Photograph of a researcher in safety glasses using a microscope"></div>
<div class="abs enteric">
  <h2>The Dangers of Enteric Coating</h2>
  <p>If you knew your Serrapeptase supplement was Enteric Coated with plastic, would you continue taking it? Phthalates, pronounced Thalates, were banned from the European Union in 2003. China and Mexico have also prohibited their use in toys. Yet the US contin-ues to use enteric coating in drugs and supplements. If the governments in various coun-tries are worried about children handling these plastic chemicals, don’t you think you should avoid ingesting them? Read more about Serrapeptase prod<br>\ucts that do not use enteric coating, but rather natural forms of acid resistant delivery methods.</p>
  <a class="outline-btn" href="#">Learn More</a>
</div>

<h2 class="abs section-title" style="top:1745px">KTB News &amp; Blog</h2>
<article class="abs post" style="left:88px">
  <div class="post-img" role="img" aria-label="Photograph of a scientist working in a stocked laboratory" style="background:linear-gradient(135deg,#7b93a8,#c9d6df 60%,#e8eef2)"><span class="post-date">22 jUL, 2019</span></div>
  <div class="post-body"><h3>Serrapeptase Review</h3><p>INTRODUCTION AND REVIEWS: Serrapeptase is also known as Serratia peptidase. The Serrapeptase enzyme is known for its pain blo...</p><a href="#">READ MORE</a></div>
</article>
<article class="abs post" style="left:436px">
  <div class="post-img" role="img" aria-label="Photograph of glass test tubes with colored liquids" style="background:linear-gradient(135deg,#dfe9ef,#b7cedb 55%,#6f9bbd)"><span class="post-date">20 Aug, 2019</span></div>
  <div class="post-body"><h3>Serrapeptase Analysis</h3><p>Serrapeptase Analysis &nbsp;&nbsp; INTRODUCTION AND REVIEWS: &nbsp; Serrapeptase is also known as serralysin, serratiapeptase, serration ...</p><a href="#">READ MORE</a></div>
</article>
<article class="abs post" style="left:786px">
  <div class="post-img" role="img" aria-label="Photograph of a gloved hand pouring liquid between laboratory flasks" style="background:linear-gradient(135deg,#9fb0c8,#c6d2e2 50%,#5fa0a8)"><span class="post-date">31 Jul, 2019</span></div>
  <div class="post-body"><h3>Serrapeptase Efficacy</h3><p>Serratiopeptidase and Its Effectiveness Serratiopeptidase, also known as serrapeptase is a common drug in Europe and Japan. ...</p><a href="#">READ MORE</a></div>
</article>

<h2 class="abs section-title" style="top:2277px">What Client Say</h2>
<div class="abs avatar" role="img" aria-label="Client profile photo"></div>
<p class="abs quote">Neque porro quisquam est, qui dolorem ipsum quia dolor sit amet, consectetur, adipisci velit, sed quia nonnumquam eius modi tempora incidunt ut labore et dolore magna aliquam quaerat voluptatem.</p>
<div class="abs client">Corwin Pell<small>Happy Client</small></div>
<div class="abs dots"><span></span><span></span><span class="on"></span></div>

<footer class="abs footer"></footer>
<div class="abs f-logo">LUMAVEXIN.KTB</div>
<p class="abs f-about">Neque porro quisquam est, qui dolorem ipsum quia dolor sit amet, consectetur, adipisci velit,</p>
<div class="abs f-col" style="left:440px;top:2597px">
  <h5>Links</h5>
  <ul class="f-links"><li>About</li><li>Contact Us</li><li>Terms &amp; Condition</li><li>Privacy Policy</li><li>Reviews</li></ul>
</div>
<div class="abs f-col" style="left:650px;top:2597px">
  <h5>Follow Us</h5>
  <ul class="f-social">
    <li><span class="dot" style="background:#2e4a8c"></span>Chatterly</li>
    <li><span class="dot" style="background:#2ba3e0"></span>Pulsebird</li>
    <li><span class="dot" style="background:#dc3b2e"></span>Searchnest</li>
    <li><span class="dot" style="background:#1f4f8f"></span>Workgrid</li>
  </ul>
</div>
<div class="abs f-col f-news" style="left:864px;top:2597px">
  <h5>Newsletter</h5>
  <p>Subscribe to our email newsletter to get weekly updates.</p>
  <div class="f-input"><svg width="12" height="9" viewBox="0 0 12 9" fill="none" stroke="#aaa"><rect x=".5" y=".5" width="11" height="8"/><path d="M.5.5L6 5l5.5-4.5"/></svg>Enter Email...</div>
  <span class="f-send">SEND</span>
</div>
<div class="abs f-rule"></div>
<div class="abs copyright">© Copyright 2019 &nbsp;|&nbsp; All Rights Reserved</div>
<div class="abs to-top"><svg width="10" height="12" viewBox="0 0 10 12" fill="none" stroke="#fff" stroke-width="1.4"><path d="M5 12V1M1 5l4-4 4 4"/></svg></div>

</body>
</html>
```